Korvel Mining Webpage

Need a website for a copper mining company that is seeking financing and /or partners with small mines. We need a website that will give basic information regarding the property we are seeking financing for, and background information of the owners (about us), current opportunity page that will convey our value added proposition, along with a 'contact us' page.

Please review other mining companies website for ideas
Any clarity needed we will communicate with you, please ask if you are uncertain.

We will likely provide more information as the design develops

Target Market(s)

Investment companies and Mining professionals

Industry/Entity Type

Mining

Number of Pages Required

4 page

Font styles to use
Sans Serif

Colors

Designer to choose colors to be used in the design.

Requirements
Must have
• I am looking to have a template which I can use later as well to add my own content. Please be sure to have each item (designs, links buttons, drop down menus)its own file so I can import into the web formats
• Also please provide primary colors used as RGB values.
• Include a list of fonts used.
• Pages see attached power point slides
• 1) About us - what we do (2 slide of the .ppt attached) need to leave room for a mission and vision statement
• 2) current opportunities (see word document and Slide 5 as results)
• 3) Value Add ideas ( pages 3)
• 4) Management (our photos Slide 4 of the deck) with room to type background information
• 5) Events and current information (this will be a page listing dates of events, and also blog entries.)
• Let us know if you can't open a .ppt file
Nice to have
• Non-cartoonish look, it should be a polished website
• Drop down menu format
• Scrolling format with an image in the background
• Contact information page (see first slide of slide deck)
• Feel free to use the photos as needed through out the site

```html
<!DOCTYPE html>
<html lang="en">
<head>
<meta charset="utf-8">
<title>Korvel Mining</title>
<link href="https://fonts.googleapis.com/css2?family=Montserrat:wght@500;600;700&family=Open+Sans:wght@400;600;700&family=Lora:wght@400;700&display=swap" rel="stylesheet">
<style>
:root{
  --navy:#1b2f63;
  --royal:#1d3d85;
  --royal-dark:#142c66;
  --ink:#222;
  --muted:#555;
  --red:#d0312d;
  --white:#fff;
  --footer:#000;
  --line:#d9d9d9;
}
*{margin:0;padding:0;box-sizing:border-box}
html,body{width:1200px;height:3871px;overflow:hidden}
body{position:relative;font-family:'Open Sans',sans-serif;color:var(--ink);background:var(--white)}
.abs{position:absolute}
.serif{font-family:'Lora',serif}

/* header */
.topbar{left:0;top:0;width:1200px;height:10px;background:var(--navy)}
.header{left:0;top:10px;width:1200px;height:150px;background:var(--white)}
.brand{left:92px;top:90px;font-family:'Lora',serif;font-size:20px;letter-spacing:2px;color:var(--ink)}
.brand-dot{left:170px;top:30px;width:44px;height:44px;border-radius:50%;background:var(--ink)}
.phone{left:846px;top:42px;font-family:'Lora',serif;font-size:22px;color:var(--ink);display:flex;align-items:center;gap:6px}
.tools{left:1040px;top:44px;display:flex;gap:16px}
.nav{right:80px;top:103px;display:flex;gap:36px;font-family:'Lora',serif;font-size:16px}
.nav span{color:var(--ink)}
.nav .active{color:var(--royal)}

/* hero */
.hero{left:0;top:160px;width:1200px;height:555px;background:linear-gradient(180deg,#8a8c8f 0%,#6f6a63 45%,#4d463e 100%)}
.hero-title{left:0;top:250px;width:1200px;text-align:center;font-family:'Montserrat',sans-serif;font-weight:600;color:var(--white);font-size:84px;line-height:1;text-shadow:0 2px 8px rgba(0,0,0,.35)}
.hero-sub{left:0;top:350px;width:1200px;text-align:center;font-family:'Montserrat',sans-serif;font-weight:600;color:var(--white);font-size:52px;text-shadow:0 2px 8px rgba(0,0,0,.35)}
.hero-arrow{top:300px;color:var(--white);font-size:28px}

/* about */
.about-frame{left:92px;top:812px;width:323px;height:438px;border:3px solid var(--navy)}
.about-photo{left:112px;top:832px;width:373px;height:398px;background:linear-gradient(160deg,#9aa0a8,#4a4e58 60%,#2c2f38)}
.about-card{left:485px;top:832px;width:615px;height:398px;background:var(--white);box-shadow:0 2px 10px rgba(0,0,0,.18);padding:36px 40px}
.about-card h2{font-family:'Lora',serif;font-weight:400;font-size:46px;color:var(--ink);margin-bottom:22px}
.about-card p{font-size:14px;line-height:28px;color:var(--muted)}
.btn{display:inline-block;margin-top:20px;background:var(--royal-dark);color:var(--white);font-size:15px;padding:9px 16px;outline:2px solid var(--royal-dark);outline-offset:3px}

/* opportunities */
.opps{left:0;top:1365px;width:1200px;height:635px;background:linear-gradient(160deg,#1d3d85,#16336f 60%,#1a3a7d)}
.section-title{left:0;width:1200px;text-align:center;font-family:'Lora',serif;font-size:44px}
.rule{width:160px;height:2px;left:520px}
.opp{top:1608px;width:267px;height:307px;border:2px solid rgba(255,255,255,.85);padding:10px}
.opp-inner{width:100%;height:100%;background:var(--white);text-align:center;padding:36px 22px 0}
.opp-icon{width:80px;height:80px;margin:0 auto 16px;border-radius:8px;background:#dfe6f4}
.opp h3{font-family:'Lora',serif;font-weight:400;font-size:19px;color:var(--ink);line-height:25px;margin-bottom:12px;min-height:25px}
.opp p{font-size:12.5px;line-height:20px;color:var(--muted)}

/* events */
.event-main{left:106px;top:2270px;width:491px;height:440px;background:var(--white);box-shadow:0 2px 10px rgba(0,0,0,.15)}
.event-main .img{width:491px;height:280px;background:linear-gradient(160deg,#5a5048,#2a2622 55%,#181614)}
.event-main .body{padding:16px 18px}
.event-main h4{font-size:18px;font-weight:700;margin-bottom:6px}
.event-main p{font-size:12px;line-height:19px;color:var(--muted)}
.more{font-size:12px;color:var(--royal);margin-top:6px}
.event-row{left:625px;width:475px;height:130px;border-bottom:1px solid var(--line)}
.event-row .thumb{position:absolute;left:0;top:0;width:180px;height:120px}
.event-row .txt{position:absolute;left:228px;top:6px;width:250px}
.event-row h5{font-size:17px;font-weight:700;margin-bottom:4px}
.event-row p{font-size:14px;line-height:21px;color:var(--muted)}
.meta{display:flex;gap:14px;margin-top:10px}

/* management */
.mgmt{left:0;top:2830px;width:1200px;height:630px;background:linear-gradient(180deg,#e9f1fb 0%,#b9d0ec 55%,#9fbde2 100%)}
.person{top:3090px;width:311px;height:305px;background:var(--white);box-shadow:0 2px 8px rgba(0,0,0,.12);text-align:center;padding-top:98px}
.avatar{top:3030px;width:136px;height:136px;border-radius:50%;border:4px solid var(--white);background:#9aa3ad}
.person h4{font-family:'Open Sans',sans-serif;font-weight:400;font-size:20px}
.role{font-size:14px;color:var(--red);margin:4px 0 10px}
.person p{font-size:14px;line-height:22px;color:var(--muted);padding:0 28px}
.socials{display:flex;gap:14px;justify-content:center;margin-top:16px}
.socials span{width:26px;height:26px;border-radius:50%;border:1.5px solid var(--royal)}
.socials span:last-child{border-color:var(--red)}
.slide-arrow{top:3220px;width:40px;height:40px;border-radius:50%;background:rgba(255,255,255,.75)}

/* footer */
.footer{left:0;top:3460px;width:1200px;height:411px;background:var(--footer);color:var(--white)}
.footer h6{font-family:'Lora',serif;font-weight:400;font-size:17px;letter-spacing:1px;margin-bottom:28px}
.fbrand{left:92px;top:3600px;font-family:'Lora',serif;font-size:20px;letter-spacing:2px}
.fcol{top:3530px}
.crow{display:flex;gap:18px;font-size:13px;line-height:21px;margin-bottom:18px}
.links li{list-style:none;font-size:13px;line-height:24px}
.links li::before{content:"▸ ";font-size:10px}
.follow{display:flex;align-items:center;gap:12px;font-size:15px;margin-bottom:20px}
.follow span.c{width:28px;height:28px;border-radius:50%;border:1.5px solid var(--white)}
.copy{left:0;top:3815px;width:1200px;text-align:center;font-size:14px}
</style>
</head>
<body>

<div class="abs topbar"></div>
<header class="abs header">
  <div class="abs brand-dot" style="left:-? "></div>
</header>
<div class="abs brand">KORVEL MINING</div>
<div class="abs phone">
  <svg width="18" height="18" viewBox="0 0 24 24" fill="#1b2f63"><path d="M6.6 10.8a15 15 0 006.6 6.6l2.2-2.2c.3-.3.7-.4 1-.2 1.1.4 2.3.6 3.6.6.6 0 1 .4 1 1V20c0 .6-.4 1-1 1A17 17 0 013 4c0-.6.4-1 1-1h3.5c.6 0 1 .4 1 1 0 1.3.2 2.5.6 3.6.1.3 0 .7-.2 1z"/></svg>
  905-410-2276
</div>
<div class="abs tools">
  <svg width="18" height="18" viewBox="0 0 24 24" fill="none" stroke="#222" stroke-width="3"><circle cx="10" cy="10" r="7"/><path d="M15 15l6 6"/></svg>
  <svg width="16" height="18" viewBox="0 0 24 24" fill="#222"><circle cx="12" cy="7" r="5"/><path d="M2 23c0-6 4-9 10-9s10 3 10 9z"/></svg>
</div>
<nav class="abs nav">
  <span class="active">Home</span><span>About us</span><span>current opportunities</span><span>Value</span><span>Management</span><span>Events</span>
</nav>

<section class="abs hero" role="img" aria-label="Photo of a pickup truck and haul truck on a mine road"></section>
<div class="abs hero-title">Korvel Mining</div>
<div class="abs hero-sub">Investor Presentation</div>
<div class="abs hero-arrow" style="left:82px">‹</div>
<div class="abs hero-arrow" style="left:1122px">›</div>

<div class="abs about-frame"></div>
<div class="abs about-photo" role="img" aria-label="Photo of miners in safety gear in an underground office"></div>
<div class="abs about-card">
  <h2>About us</h2>
  <p>It is a long established fact that a reader will be distracted by the readable content of a page when looking at its layout. The point of using Lorem Ipsum is that it has a more-or-less normal distribution of letters, as opposed to using 'Content here, content here', making it look like readable English. Many desktop publishing packages and web page editors now use Lorem Ipsum as their default model text, and a search for 'lorem ipsum' will uncover</p>
  <span class="btn">Read More</span>
</div>

<section class="abs opps" role="img" aria-label="Blue tinted mountain landscape background"></section>
<h2 class="abs section-title" style="top:1470px;color:var(--white);font-weight:400">Current Opportunities</h2>
<div class="abs rule" style="top:1540px;background:var(--white)"></div>
<div class="abs opp" style="left:170px"><div class="opp-inner"><div class="opp-icon" role="img" aria-label="Financial charts icon"></div><h3>Financial Metrics</h3><p>Lorem Ipsum has been the industry's standard dummy text ever since the 1500s, when</p></div></div>
<div class="abs opp" style="left:468px"><div class="opp-inner" style="padding-top:28px"><div class="opp-icon" role="img" aria-label="Mining tools icon"></div><h3>Base Case Op Improvements</h3><p>Lorem Ipsum has been the industry's standard dummy text ever since the 1500s, when</p></div></div>
<div class="abs opp" style="left:780px"><div class="opp-inner"><div class="opp-icon" role="img" aria-label="Miner with equipment icon"></div><h3>Mill + Exploration</h3><p>Lorem Ipsum has been the industry's standard dummy text ever since the 1500s, when</p></div></div>

<h2 class="abs section-title" style="top:2138px;color:var(--ink);font-weight:400">Events and Current information</h2>
<div class="abs rule" style="top:2206px;background:var(--ink)"></div>

<article class="abs event-main">
  <div class="img" role="img" aria-label="Photo of miners with headlamps in an underground tunnel"></div>
  <div class="body">
    <h4>Neque porro quisquam est qui dolorem</h4>
    <p>It is a long established fact that a reader will be distracted by the readable content of a page when looking at its layout. The point of using Lorem Ipsum is that it has a more-or-less normal distribution</p>
    <div class="more">Read More »</div>
  </div>
</article>

<article class="abs event-row" style="top:2275px">
  <div class="thumb" role="img" aria-label="Photo of a mine office interior" style="background:linear-gradient(160deg,#8c8f94,#3e4048)"></div>
  <div class="txt"><h5>Neque porro quisquam est</h5><p>Ipsum is simply dummy text of the printing and type page when</p>
  <div class="meta"><svg width="18" height="18" viewBox="0 0 24 24" fill="none" stroke="#777" stroke-width="1.5"><path d="M12 2l3 7h7l-5.5 4.5 2 7.5-6.5-4.5-6.5 4.5 2-7.5L2 9h7z"/></svg><svg width="18" height="18" viewBox="0 0 24 24" fill="none" stroke="#777" stroke-width="1.5"><rect x="3" y="5" width="18" height="16"/><path d="M3 10h18M8 3v4M16 3v4"/></svg><svg width="18" height="18" viewBox="0 0 24 24" fill="none" stroke="#777" stroke-width="1.5"><circle cx="12" cy="8" r="4"/><path d="M4 21c0-5 4-7 8-7s8 2 8 7"/></svg></div></div>
</article>
<article class="abs event-row" style="top:2430px">
  <div class="thumb" role="img" aria-label="Photo of ore processing machinery" style="background:linear-gradient(160deg,#7a5a3a,#2e2a26)"></div>
  <div class="txt"><h5>Porro quisquam est dolorem</h5><p>Ipsum is simply dummy text of the printing and type page when</p>
  <div class="meta"><svg width="18" height="18" viewBox="0 0 24 24" fill="none" stroke="#777" stroke-width="1.5"><path d="M12 2l3 7h7l-5.5 4.5 2 7.5-6.5-4.5-6.5 4.5 2-7.5L2 9h7z"/></svg><svg width="18" height="18" viewBox="0 0 24 24" fill="none" stroke="#777" stroke-width="1.5"><rect x="3" y="5" width="18" height="16"/><path d="M3 10h18M8 3v4M16 3v4"/></svg><svg width="18" height="18" viewBox="0 0 24 24" fill="none" stroke="#777" stroke-width="1.5"><circle cx="12" cy="8" r="4"/><path d="M4 21c0-5 4-7 8-7s8 2 8 7"/></svg></div></div>
</article>
<article class="abs event-row" style="top:2585px;border-bottom:none">
  <div class="thumb" role="img" aria-label="Photo of a steel grinding mill drum" style="background:linear-gradient(160deg,#b0b2b5,#5c5e62)"></div>
  <div class="txt"><h5>Dolorem ipsum quia dolor</h5><p>Ipsum is simply dummy text of the printing and type page when</p>
  <div class="meta"><svg width="18" height="18" viewBox="0 0 24 24" fill="none" stroke="#777" stroke-width="1.5"><path d="M12 2l3 7h7l-5.5 4.5 2 7.5-6.5-4.5-6.5 4.5 2-7.5L2 9h7z"/></svg><svg width="18" height="18" viewBox="0 0 24 24" fill="none" stroke="#777" stroke-width="1.5"><rect x="3" y="5" width="18" height="16"/><path d="M3 10h18M8 3v4M16 3v4"/></svg><svg width="18" height="18" viewBox="0 0 24 24" fill="none" stroke="#777" stroke-width="1.5"><circle cx="12" cy="8" r="4"/><path d="M4 21c0-5 4-7 8-7s8 2 8 7"/></svg></div></div>
</article>

<section class="abs mgmt" role="img" aria-label="Light blue city skyline background"></section>
<h2 class="abs section-title" style="top:2900px;color:var(--ink);font-weight:400">Management</h2>
<div class="abs rule" style="top:2966px;background:var(--ink)"></div>
<div class="abs slide-arrow" style="left:52px"><svg width="40" height="40" viewBox="0 0 40 40" fill="none" stroke="#555" stroke-width="2"><path d="M23 12l-8 8 8 8"/></svg></div>
<div class="abs slide-arrow" style="left:1118px"><svg width="40" height="40" viewBox="0 0 40 40" fill="none" stroke="#555" stroke-width="2"><path d="M17 12l8 8-8 8"/></svg></div>

<div class="abs person" style="left:112px"><h4>Lena Varkosa</h4><div class="role">Legal Consul</div><p>15 yr mining experience<br>Local Counsel for Valle Abierto Project(Cerro Lunar-Pallca)</p><div class="socials"><span></span><span></span><span></span></div></div>
<div class="abs person" style="left:450px"><h4>Tomas Reyvel</h4><div class="role">COO</div><p>9 yr mining experience<br>Current General Manager of Santa Brena &amp; Unión</p><div class="socials"><span></span><span></span><span></span></div></div>
<div class="abs person" style="left:790px"><h4>Daniel Ostrand</h4><div class="role">CEO</div><p>13 yr mining experience<br>Masters in Mining Engineering from Redrock Institute of Mines.</p><div class="socials"><span></span><span></span><span></span></div></div>
<div class="abs avatar" role="img" aria-label="Portrait photo of the legal consul" style="left:200px;background:#b89c86"></div>
<div class="abs avatar" role="img" aria-label="Portrait photo of the COO" style="left:538px;background:#8a8f99"></div>
<div class="abs avatar" role="img" aria-label="Portrait photo of the CEO" style="left:878px;background:#7d8088"></div>

<footer class="abs footer"></footer>
<div class="abs fbrand">KORVEL MINING</div>
<div class="abs fcol" style="left:392px">
  <h6>CONTACT US</h6>
  <div class="crow"><svg width="14" height="18" viewBox="0 0 24 30" fill="#fff"><path d="M12 0a10 10 0 00-10 10c0 8 10 20 10 20s10-12 10-20A10 10 0 0012 0zm0 14a4 4 0 110-8 4 4 0 010 8z"/></svg><div>218 Harlow Street 4th Floor<br>Brenford, NY 10457</div></div>
  <div class="crow"><svg width="14" height="14" viewBox="0 0 24 24" fill="#fff"><path d="M6.6 10.8a15 15 0 006.6 6.6l2.2-2.2c.3-.3.7-.4 1-.2 1.1.4 2.3.6 3.6.6.6 0 1 .4 1 1V20c0 .6-.4 1-1 1A17 17 0 013 4c0-.6.4-1 1-1h3.5c.6 0 1 .4 1 1 0 1.3.2 2.5.6 3.6.1.3 0 .7-.2 1z"/></svg><div>914-550-1382</div></div>
  <div class="crow"><svg width="14" height="14" viewBox="0 0 24 24" fill="#fff"><path d="M2 5h20v14H2z"/><path d="M2 5l10 8 10-8" stroke="#000" stroke-width="2" fill="none"/></svg><div>info@korvelmining.com</div></div>
</div>
<div class="abs fcol" style="left:735px">
  <h6>QUICK LINKS</h6>
  <ul class="links"><li>Home</li><li>About Us</li><li>Services</li><li>News</li><li>Contact Us</li></ul>
</div>
<div class="abs fcol" style="left:958px">
  <h6>FOLLOW US</h6>
  <div class="follow"><span class="c"></span>Facefeed</div>
  <div class="follow"><span class="c"></span>Snapgram</div>
  <div class="follow"><span class="c"></span>Circles+</div>
</div>
<div class="abs copy">© Copyright 2019 . All Rights Reserved.</div>

</body>
</html>
```